New Brand - Website Design (4 Pages)

We are launching a new brand for electronic cigarettes. We already have logo and packaging done and would like a web design to go with it.

We are interested in the following deliverables:

1) Home Page Design
2) Check Out Design
3) How it Works Page
4) Secondary Template Page Design

Looking for a 60s modern look and something that is consistent with our logo and packaging.

Industry/Entity Type

Electronic

Requirements
Must have
• Consistent with logo and packaging (Use Logo Attached)
White background

Example (Functionality & Design): http://www.torvex.co.uk/
Example (Design): http://www.quillharbor.com/

We want the design more like quillharbor but the functionality the same as torvex.

Top Bar: Pebble Arcs Kits; Cartridge Refills; How it Works; Contact; My Account; Checkout
Should not have
• Stock List or Search Bar or Newsletter Signup

```html
<!DOCTYPE html>
<html lang="en">
<head>
<meta charset="utf-8">
<title>Pebble Arcs – Secondary Page</title>
<link href="https://fonts.googleapis.com/css2?family=Josefin+Sans:wght@400;600&family=Quicksand:wght@300;400;500&display=swap" rel="stylesheet">
<style>
  :root {
    --page-bg-light: #f7f7f7;
    --page-bg-dark: #d9d9d9;
    --stripe: rgba(0,0,0,0.035);
    --panel: #ffffff;
    --ink: #1c1c1c;
    --band: #000000;
    --band-text: #e2e2e2;
    --rule: #8a8a8a;
    --sky: #8dd6f6;
    --ghost: #ececec;
    --footer-text: #333333;
  }
  * { box-sizing: border-box; margin: 0; padding: 0; }
  html, body { width: 1127px; height: 1200px; overflow: hidden; }
  body {
    position: relative;
    font-family: "Quicksand", sans-serif;
    color: var(--ink);
    background:
      repeating-linear-gradient(90deg, var(--stripe) 0 2px, transparent 2px 6px),
      linear-gradient(180deg, var(--page-bg-light) 0%, var(--page-bg-light) 45%, var(--page-bg-dark) 100%);
  }
  .page {
    position: absolute; left: 67px; top: 36px; width: 984px; height: 1094px;
    background: var(--panel);
    box-shadow: 2px 3px 6px rgba(0,0,0,0.35);
  }
  .masthead {
    position: absolute; left: 0; top: 0; width: 100%; height: 198px;
    background: linear-gradient(180deg, #ffffff 0%, #ffffff 40%, #ebebeb 100%);
  }
  .brand-name {
    position: absolute; left: 0; top: 76px; width: 100%; text-align: center;
    font-family: "Josefin Sans", sans-serif; font-weight: 600;
    font-size: 56px; letter-spacing: 3px; color: var(--ink); text-transform: uppercase;
  }
  .main-nav {
    position: absolute; left: 0; top: 244px; width: 1127px; height: 43px;
    background: #fff; border: 1px solid #bdbdbd;
    box-shadow: 0 2px 4px rgba(0,0,0,0.25);
    display: flex; justify-content: center; align-items: center;
    font-size: 17px; letter-spacing: 1px; z-index: 2;
  }
  .main-nav a { color: var(--ink); text-decoration: none; }
  .main-nav .sep { margin: 0 6px; }
  .flavors {
    position: absolute; left: 0; top: 251px; width: 100%; height: 296px;
    background: var(--band);
    box-shadow: 0 4px 8px rgba(0,0,0,0.35);
  }
  .flavors-title {
    position: absolute; left: 0; top: 23px; width: 100%; text-align: center;
    font-family: "Josefin Sans", sans-serif; font-size: 27px; letter-spacing: 3.5px; color: #fff;
  }
  .rule { position: absolute; top: 38px; height: 1px; background: var(--rule); }
  .rule.left { left: 17px; width: 372px; }
  .rule.right { left: 597px; width: 369px; }
  .flavor { position: absolute; top: 109px; width: 180px; text-align: center; }
  .flavor-art {
    width: 64px; height: 72px; margin: 0 auto 20px;
    background: #1e4e63; border-radius: 6px;
  }
  .flavor-name { font-size: 18px; letter-spacing: 1.5px; color: var(--band-text); }
  .dot { position: absolute; top: 198px; width: 15px; height: 15px; border-radius: 50%; background: #fff; }
  .content-title {
    position: absolute; left: 0; top: 692px; width: 100%; text-align: center;
    font-size: 43px; font-weight: 300; letter-spacing: 4px; color: var(--ghost);
  }
  .buy-band {
    position: absolute; left: 0; top: 930px; width: 100%; height: 121px;
    background: var(--sky);
    display: flex; justify-content: center; align-items: center;
    font-family: "Josefin Sans", sans-serif; font-weight: 600;
    font-size: 29px; letter-spacing: 3.5px; color: var(--ink); text-decoration: none;
  }
  .site-footer {
    position: absolute; left: 0; top: 1163px; width: 100%; text-align: center;
    font-size: 13px; color: var(--footer-text);
  }
</style>
</head>
<body>
  <div class="page">
    <header class="masthead">
      <div class="brand-name">Pebble Arcs</div>
    </header>

    <section class="flavors">
      <span class="rule left"></span>
      <h2 class="flavors-title">FLAVORS</h2>
      <span class="rule right"></span>

      <div class="flavor" style="left:51px"><div class="flavor-art" role="img" aria-label="Line drawing of a tobacco leaf"></div><div class="flavor-name">Tobacco Classic</div></div>
      <div class="flavor" style="left:237px"><div class="flavor-art" role="img" aria-label="Line drawing of mint leaves"></div><div class="flavor-name">Menthol</div></div>
      <div class="flavor" style="left:414px"><div class="flavor-art" role="img" aria-label="Line drawing of a banana"></div><div class="flavor-name">Banana</div></div>
      <div class="flavor" style="left:589px;top:107px"><div class="flavor-art" role="img" aria-label="Line drawing of an apple"></div><div class="flavor-name">Apple</div></div>
      <div class="flavor" style="left:766px;top:107px"><div class="flavor-art" role="img" aria-label="Line drawing of a thumbs-up hand in a circle"></div><div class="flavor-name">Non-Nicotine</div></div>

      <span class="dot" style="left:245px"></span>
      <span class="dot" style="left:398px"></span>
      <span class="dot" style="left:575px"></span>
      <span class="dot" style="left:752px"></span>
    </section>

    <h1 class="content-title">Secondary Page</h1>

    <a class="buy-band" href="#">BUY NOW</a>
  </div>

  <nav class="main-nav">
    <a href="#">Home</a><span class="sep">|</span>
    <a href="#">Pebble Arcs Kits</a><span class="sep">|</span>
    <a href="#">Cartridge Refills</a><span class="sep">|</span>
    <a href="#">How it Works</a><span class="sep">|</span>
    <a href="#">Contact</a><span class="sep">|</span>
    <a href="#">My Account</a><span class="sep">|</span>
    <a href="#">Checkout</a>
  </nav>

  <footer class="site-footer">Copyright 2013 PebbleArcs - Terms &amp; Conditions | Privacy Policy</footer>
</body>
</html>
```